Landing page for a cyber security service provider called 'Lumen Grove'

The client is a new cyber security company in need of a website landing page at lumengrove.example.

Their visual identity is modern, playful, clean and uncluttered and represents innovation, connectivity and approachability.

The company logo is provided in black (attached) but the client is open to changing the colour to align with the new website design.

The landing page needs to contain:
- A call to action with a 'Get Started' button
-Links to blank 'How it works', 'Products', 'Pricing', 'About Us' and 'Contact Us' pages (that we'll fill out later)

Target Market(s)

Medium to large businesses who probably don't understand cyber / cyber security but need their business to be protected.

Industry/Entity Type

Cyber Security

Coding

Coded - Design and coding required

Number of Pages Required

1 page

Font styles to use
Sans Serif
Other font styles liked:
• Helvetica

Requirements
Nice to have
• Hero banner at the top of the landing page.
Should not have
• Should not look like a traditional cyber / cyber security design (eg no dark blue/ black, red/black colour combinations). Please no military styles (eg no shields, cannons, swords, guns)

```html
<!DOCTYPE html>
<html lang="en">
<head>
<meta charset="utf-8">
<title>Lumen Grove — Cyber Security Services</title>
<link rel="stylesheet" href="https://fonts.googleapis.com/css2?family=Arimo:ital,wght@0,400;0,700;1,700&family=Lato:wght@400;700&display=swap">
<style>
:root{
  --ink:#1a1a1a;
  --band:#0e5c56;
  --band-deep:#094540;
  --band-light:#2f8a80;
  --sun:#fcbf3a;
  --sun-soft:#fdf1d2;
  --paper:#ffffff;
  --mist:#eef5f3;
  --text:#1a1a1a;
  --muted:#3a3a3a;
  --head:"Arimo",Helvetica,Arial,sans-serif;
  --body:"Lato",Helvetica,Arial,sans-serif;
}
*{box-sizing:border-box;margin:0;padding:0}
html,body{width:1200px;height:3841px;overflow:hidden;background:var(--paper)}
body{font-family:var(--body);color:var(--text)}
.page{position:relative;width:1200px;height:3841px;overflow:hidden}
.abs{position:absolute}
a{color:inherit;text-decoration:none}

/* buttons */
.btn{position:absolute;display:flex;align-items:center;justify-content:space-between;height:40px;border-radius:20px;padding:0 6px 0 24px;font-family:var(--head);font-weight:700;font-size:14px;color:var(--ink)}
.btn--sun{background:var(--sun)}
.btn--light{background:var(--paper)}
.btn__dot{width:28px;height:28px;border-radius:50%;background:var(--band);display:flex;align-items:center;justify-content:center}

/* hero */
.hero{position:absolute;left:0;top:0;width:1200px;height:604px;background:var(--band);overflow:hidden}
.hero__art{position:absolute;left:600px;top:0;width:600px;height:540px;background:radial-gradient(ellipse at 55% 50%,var(--band-light) 0%,var(--band) 50%,var(--band) 80%)}
.brand{position:absolute;font-family:var(--head);font-weight:700;display:flex;align-items:center;gap:8px}
.brand__dot{border-radius:50%;border:3px solid currentColor}
.nav{position:absolute;left:375px;top:40px;display:flex;gap:24px;font-family:var(--head);font-size:13px;color:var(--paper)}
.phone{position:absolute;left:782px;top:39px;display:flex;gap:8px;align-items:center;font-family:var(--head);font-weight:700;font-size:15px;color:var(--paper)}
.nav-cta{position:absolute;left:937px;top:33px;width:114px;height:32px;border-radius:16px;background:var(--sun);font-family:var(--head);font-weight:700;font-size:13px;color:var(--ink);display:flex;align-items:center;justify-content:center}
.hero__title{position:absolute;left:150px;top:166px;font-family:var(--head);font-weight:700;font-size:56px;color:var(--paper);line-height:1}
.hero__sub{position:absolute;left:150px;top:226px;font-family:var(--head);font-weight:700;font-size:40px;color:var(--sun);line-height:46px}
.hero__sub em{font-style:italic;display:block}
.hero__lede{position:absolute;left:150px;top:333px;width:410px;font-size:14px;line-height:20px;color:var(--paper)}

/* about */
.about__photo{position:absolute;left:170px;top:655px;width:396px;height:396px;border-radius:50%;background:linear-gradient(135deg,#9a7250,#5d4431 55%,#c9c9c9)}
.about__arc{position:absolute;left:198px;top:700px;width:390px;height:390px;border-radius:50%;background:var(--sun)}
.about__thumb{position:absolute;left:406px;top:945px;width:178px;height:178px;border-radius:50%;border:6px solid var(--paper);background:radial-gradient(circle at 50% 45%,#3f7f7a,#0f2a2c 70%)}
.section-title{font-family:var(--head);font-size:48px;font-weight:400;line-height:1;color:var(--ink)}
.section-title .hl{color:var(--sun);font-weight:400}
.section-title b{font-weight:700}
.about__title{position:absolute;left:634px;top:686px}
.about__lead{position:absolute;left:634px;top:742px;width:330px;font-weight:700;font-size:14px;line-height:18px;color:var(--ink)}
.about__copy{position:absolute;left:634px;top:787px;width:420px;font-size:13.5px;line-height:20.5px;color:var(--muted)}
.about__copy p+p{margin-top:20px}

/* how it works */
.how__title{position:absolute;left:0;top:1318px;width:1200px;text-align:center;font-family:var(--head);font-size:44px;font-weight:700;color:var(--paper)}
.how__title span{color:var(--sun);font-weight:400}
.how__lede{position:absolute;left:400px;top:1378px;width:400px;text-align:center;font-size:14px;line-height:19px;color:var(--paper)}
.step{position:absolute;width:250px;color:var(--paper)}
.step h3{font-family:var(--head);font-weight:700;font-size:22px;color:var(--sun);margin-bottom:8px}
.step p{font-size:13px;line-height:19px}
.step--right{text-align:right}
.hub-label{font-family:var(--head);font-weight:700;font-size:17px;fill:var(--ink)}
.node-num{font-family:var(--head);font-weight:700;font-size:24px;fill:var(--paper)}

/* products */
.products__title{position:absolute;left:150px;top:2126px;font-size:36px}
.products__lede{position:absolute;left:631px;top:2124px;width:420px;font-size:13.5px;line-height:20px;color:var(--muted)}
.card{position:absolute;top:2206px;width:292px;height:380px;background:linear-gradient(180deg,#ffffff 0%,var(--sun-soft) 100%);box-shadow:0 4px 14px rgba(0,0,0,.12);text-align:center}
.card__img{width:176px;height:176px;border-radius:50%;margin:24px auto 0}
.card h3{font-family:var(--head);font-weight:700;font-size:20px;margin-top:28px;color:var(--ink)}
.card p{font-size:13px;line-height:19px;color:var(--muted);margin:14px 24px 0}

/* contact */
.contact-card{position:absolute;left:160px;top:2896px;width:448px;height:512px;border-radius:16px;background:var(--sun);overflow:hidden}
.contact-card__head{height:72px;background:var(--paper);text-align:center;font-family:var(--head);font-size:38px;font-weight:400;line-height:76px;color:var(--ink)}
.contact-card__rule{position:absolute;left:170px;top:90px;width:110px;height:3px;background:var(--ink)}
.field{position:absolute;border:1px solid rgba(0,0,0,.35);border-radius:6px;font-family:var(--head);font-size:12px;padding:14px 18px;color:var(--ink)}

/* footer */
.footer{position:absolute;left:0;top:3390px;width:1200px;height:420px;background:linear-gradient(180deg,#ffffff 0%,var(--mist) 100%)}
.footer__nav{position:absolute;left:0;top:3668px;width:1200px;display:flex;justify-content:center;gap:26px;font-family:var(--head);font-weight:700;font-size:13.5px;color:var(--ink)}
.social{position:absolute;top:3714px;width:36px;height:36px;border-radius:50%;border:2px solid var(--band);background:var(--paper)}
.legal{position:absolute;left:0;top:3810px;width:1200px;height:31px;background:var(--band);color:var(--paper);text-align:center;font-family:var(--head);font-size:10px;line-height:31px}
</style>
</head>
<body>
<div class="page">

  <!-- Hero -->
  <header class="hero">
    <div class="hero__art" role="img" aria-label="Hand holding a glowing padlock with data protection icons"></div>
    <svg class="abs" style="left:0;top:0" width="1200" height="604" viewBox="0 0 1200 604">
      <path d="M0 592 C 320 570 640 560 860 500 C 1020 455 1130 420 1200 372 L1200 604 L0 604 Z" fill="#ffffff"/>
      <path d="M0 592 C 320 570 640 560 860 500 C 1020 455 1130 420 1200 372" fill="none" stroke="#fcbf3a" stroke-width="12"/>
    </svg>

    <a class="brand" href="#" style="left:150px;top:52px;font-size:22px;color:#fff">
      <span class="brand__dot" style="width:18px;height:18px"></span>Lumen Grove
    </a>
    <nav class="nav">
      <a href="#">Home</a><a href="#">How it works</a><a href="#">Products</a><a href="#">Pricing</a><a href="#">About Us</a>
    </nav>
    <div class="phone">
      <svg width="16" height="16" viewBox="0 0 24 24"><path fill="#fcbf3a" d="M6.6 10.8a15 15 0 0 0 6.6 6.6l2.2-2.2c.3-.3.7-.4 1-.2 1.1.4 2.3.6 3.6.6.6 0 1 .4 1 1V20c0 .6-.4 1-1 1A17 17 0 0 1 3 4c0-.6.4-1 1-1h3.5c.6 0 1 .4 1 1 0 1.3.2 2.5.6 3.6.1.3 0 .7-.2 1z"/></svg>
      1080 555 0147
    </div>
    <a class="nav-cta" href="#">Contact Us</a>

    <h1 class="hero__title">Cyber Security</h1>
    <p class="hero__sub">Service Provider Called<em>‘Lumen Grove’</em></p>
    <p class="hero__lede">Sed at volutpat lacus, fermentum interdum libero. Suspendisse eleifend velit ac dolor porttitor, non congue lacus interdum.</p>

    <a class="btn btn--sun" href="#" style="left:150px;top:396px;width:140px">Get Started
      <span class="btn__dot"><svg width="10" height="10" viewBox="0 0 10 10"><path d="M3 1l4 4-4 4" fill="none" stroke="#fff" stroke-width="2"/></svg></span></a>
    <a class="btn btn--light" href="#" style="left:303px;top:396px;width:141px">Contact Us
      <span class="btn__dot"><svg width="10" height="10" viewBox="0 0 10 10"><path d="M3 1l4 4-4 4" fill="none" stroke="#fff" stroke-width="2"/></svg></span></a>
  </header>

  <!-- About -->
  <section class="about">
    <div class="about__arc"></div>
    <div class="about__photo" role="img" aria-label="Hands typing on a laptop showing a cyber security login screen"></div>
    <div class="about__thumb" role="img" aria-label="Computer monitor displaying a glowing padlock"></div>
    <h2 class="section-title about__title"><span class="hl">About</span> <b>Us</b></h2>
    <p class="about__lead">Curabitur efficitur auctor diam, non hendrerit dui mattis sed.</p>
    <div class="about__copy">
      <p>Donec laoreet mi id risus porta, vitae pharetra diam volutpat. Duis sit amet risus est. Ut posuere, magna et vestibulum facilisis, mi ante blandit felis, eget placerat arcu nisl vitae augue. Donec tincidunt hendrerit nisi quis gravida.</p>
      <p>Etiam tincidunt, urna id gravida rhoncus, ipsum orci auctor elit, a semper mi justo vitae tortor. In lobortis a est at pellentesque. Vivamus at turpis aliquam ligula luctus eleifend. In eget nunc libero. Sed cursus, urna a feugiat mattis, purus purus gravida est, in tempus libero sem in nisl.</p>
    </div>
    <a class="btn btn--sun" href="#" style="left:634px;top:1013px;width:134px">Read More
      <span class="btn__dot"><svg width="10" height="10" viewBox="0 0 10 10"><path d="M3 1l4 4-4 4" fill="none" stroke="#fff" stroke-width="2"/></svg></span></a>
  </section>

  <!-- How it works -->
  <section class="how">
    <svg class="abs" style="left:0;top:1160px" width="1200" height="920" viewBox="0 0 1200 920">
      <path d="M0 205 C 260 80 620 110 1200 15 L1200 710 C 1050 820 800 860 0 897 Z" fill="#0e5c56"/>
      <path d="M0 205 C 260 80 620 110 1200 15" fill="none" stroke="#fcbf3a" stroke-width="14"/>
      <path d="M1200 710 C 1050 820 800 860 0 897" fill="none" stroke="#fcbf3a" stroke-width="12"/>
    </svg>
    <h2 class="how__title">How It <span>Work</span></h2>
    <p class="how__lede">In hac habitasse platea dictumst. Vivamus aliquet eu quam id malesuada. Curabitur et finibus urna, ac pellentesque lacus.</p>

    <svg class="abs" style="left:0;top:1460px" width="1200" height="440" viewBox="0 1460 1200 440">
      <g stroke="#ffffff" stroke-width="8" stroke-linecap="round">
        <line x1="510" y1="1530" x2="597" y2="1704"/>
        <line x1="786" y1="1671" x2="597" y2="1704"/>
        <line x1="719" y1="1844" x2="597" y2="1704"/>
        <line x1="455" y1="1848" x2="597" y2="1704"/>
      </g>
      <circle cx="597" cy="1704" r="68" fill="#fcbf3a" stroke="#ffffff" stroke-width="6"/>
      <text class="hub-label" x="597" y="1710" text-anchor="middle">Lumen Grove</text>
      <g fill="#094540" stroke="#ffffff" stroke-width="6">
        <circle cx="510" cy="1530" r="34"/>
        <circle cx="786" cy="1671" r="34"/>
        <circle cx="719" cy="1844" r="34"/>
        <circle cx="455" cy="1848" r="34"/>
      </g>
      <text class="node-num" x="510" y="1539" text-anchor="middle">1</text>
      <text class="node-num" x="786" y="1680" text-anchor="middle">2</text>
      <text class="node-num" x="719" y="1853" text-anchor="middle">3</text>
      <text class="node-num" x="455" y="1857" text-anchor="middle">4</text>
    </svg>

    <div class="step step--right" style="left:202px;top:1477px"><h3>Integer gravida</h3><p>In hac habitasse platea dictumst. Vivamus aliquet eu quam id malesuada. Curabitur et finibus urna, ac pellentesque lacus.</p></div>
    <div class="step" style="left:842px;top:1612px"><h3>Pellentesque nisl</h3><p>In hac habitasse platea dictumst. Vivamus aliquet eu quam id malesuada. Curabitur et finibus urna, ac pellentesque lacus.</p></div>
    <div class="step step--right" style="left:150px;top:1798px"><h3>Proin blandit id</h3><p>Vestibulum quis bibendum erat. Mauris quis justo eros. Aenean ultricies interdum mauris.</p></div>
    <div class="step" style="left:775px;top:1801px;width:260px"><h3>Vivamus sed</h3><p>In hac habitasse platea dictumst. Vivamus aliquet eu quam id malesuada. Curabitur et finibus urna, ac pellentesque lacus.</p></div>
  </section>

  <!-- Products -->
  <section class="products">
    <h2 class="section-title products__title"><span class="hl">Our</span> Products</h2>
    <p class="products__lede">Sed leo sem, tincidunt a nulla eu, posuere cursus ex. Sed euismod sapien eget odio maximus semper non id justo.</p>

    <article class="card" style="left:150px">
      <div class="card__img" role="img" aria-label="Hand holding a phone with a security app" style="background:radial-gradient(circle at 50% 50%,#2b6fd6,#1a1f33 60%,#6b5a4a)"></div>
      <h3>Vivamus aliquet</h3>
      <p>Vestibulum fringilla justo nibh, volutpat convallis felis ullamcorper eu. Vestibulum ornare suscipit iaculis.</p>
    </article>
    <article class="card" style="left:456px">
      <div class="card__img" role="img" aria-label="Hands typing on a laptop with glowing network icons" style="background:radial-gradient(circle at 50% 55%,#3a4a55,#1f9ac8 60%,#7fd0ea)"></div>
      <h3>Curabitur et finibus</h3>
      <p>Vestibulum fringilla justo nibh, volutpat convallis felis ullamcorper eu. Vestibulum ornare suscipit iaculis.</p>
    </article>
    <article class="card" style="left:760px">
      <div class="card__img" role="img" aria-label="Combination padlock on a grey surface" style="background:radial-gradient(circle at 45% 45%,#d8d8d8,#8a8a8a 55%,#3a3a3a)"></div>
      <h3>Integer gravida orci</h3>
      <p>Vestibulum fringilla justo nibh, volutpat convallis felis ullamcorper eu. Vestibulum ornare suscipit iaculis.</p>
    </article>

    <svg class="abs" style="left:966px;top:2611px" width="90" height="22" viewBox="0 0 90 22">
      <g fill="none" stroke="#1a1a1a" stroke-width="1.8" stroke-linecap="round">
        <path d="M2 11h34M10 3L2 11l8 8"/>
        <path d="M52 11h34M78 3l8 8-8 8"/>
      </g>
    </svg>
  </section>

  <!-- Contact -->
  <section class="contact">
    <svg class="abs" style="left:0;top:2670px" width="1200" height="740" viewBox="0 0 1200 740">
      <defs>
        <clipPath id="contact-band"><path d="M0 222 C 300 90 700 40 1200 10 L1200 580 C 1000 660 800 700 600 712 L0 714 Z"/></clipPath>
        <linearGradient id="contact-photo" x1="0" y1="0" x2="1" y2="1">
          <stop offset="0" stop-color="#3c5a5e"/><stop offset=".5" stop-color="#6b8a8c"/><stop offset="1" stop-color="#2c4446"/>
        </linearGradient>
      </defs>
      <path d="M0 222 C 300 90 700 40 1200 10 L1200 580 C 1000 660 800 700 600 712 L0 714 Z" fill="#0e5c56"/>
      <g role="img" aria-label="Businessman working on a laptop with online customer assistance graphics" clip-path="url(#contact-band)">
        <rect x="560" y="0" width="640" height="740" fill="url(#contact-photo)"/>
      </g>
      <path d="M0 222 C 300 90 700 40 1200 10" fill="none" stroke="#fcbf3a" stroke-width="14"/>
      <path d="M1200 580 C 1000 660 800 700 600 712" fill="none" stroke="#fcbf3a" stroke-width="10"/>
    </svg>

    <form class="contact-card" action="#">
      <div class="contact-card__head">Contact <b>Now</b></div>
      <span class="contact-card__rule"></span>
      <div class="field" style="left:35px;top:101px;width:378px;height:48px">Name</div>
      <div class="field" style="left:35px;top:161px;width:185px;height:48px">Email</div>
      <div class="field" style="left:228px;top:161px;width:185px;height:48px">Phone Number</div>
      <div class="field" style="left:35px;top:222px;width:378px;height:142px">Message</div>
      <a class="btn btn--light" href="#" style="left:170px;top:415px;width:110px;height:40px;padding-left:24px">Submit
        <span class="btn__dot"><svg width="10" height="10" viewBox="0 0 10 10"><path d="M3 1l4 4-4 4" fill="none" stroke="#fff" stroke-width="2"/></svg></span></a>
    </form>
  </section>

  <!-- Footer -->
  <footer>
    <div class="footer"></div>
    <a class="brand" href="#" style="left:0;top:3580px;width:1200px;justify-content:center;font-size:34px;color:#0e5c56">
      <span class="brand__dot" style="width:26px;height:26px"></span>Lumen Grove
    </a>
    <nav class="footer__nav">
      <a href="#">Home</a><a href="#">How it works</a><a href="#">Products</a><a href="#">Pricing</a><a href="#">About Us</a><a href="#">Contact Us</a>
    </nav>
    <a class="social" href="#" style="left:527px" aria-label="Social profile one"></a>
    <a class="social" href="#" style="left:582px" aria-label="Social profile two"></a>
    <a class="social" href="#" style="left:639px" aria-label="Social profile three"></a>
    <p class="legal">Copyright © 2024 Lumen Grove. All rights reserved.</p>
  </footer>

</div>
</body>
</html>
```